Back Pain

Need a flyer similar to the attached draft. This is to be handed out to prospective patients. Note that Sketch Hive has already designed the logo. If you need a copy please contact me

```html
<!DOCTYPE html>
<html lang="en">
<head>
<meta charset="utf-8">
<title>Spine Ease Clinic – Tech Neck Flyer</title>
<link href="https://fonts.googleapis.com/css2?family=Montserrat:wght@600;700;800&family=Open+Sans:wght@400;500&display=swap" rel="stylesheet">
<style>
  :root{
    --blue:#0b6db8;
    --sky:#29aae2;
    --teal:#174a6b;
    --green:#8cc63f;
    --band:rgba(92,136,196,.86);
    --white:#ffffff;
  }
  *{margin:0;padding:0;box-sizing:border-box}
  html,body{width:927px;height:1200px;overflow:hidden;background:#fff}
  .flyer{position:relative;width:1000px;height:1294px;transform:scale(.927);transform-origin:0 0;background:var(--blue);font-family:"Montserrat",sans-serif;color:var(--white);overflow:hidden}
  .abs{position:absolute}
  .hero-photo{left:0;top:0;width:1000px;height:440px;background:linear-gradient(100deg,#e9e9e7 0%,#f4f3f1 40%,#e3e2df 60%,#f7f7f6 100%)}
  .brand{right:18px;top:70px;width:370px;text-align:center}
  .brand-mark{width:84px;height:84px;border-radius:50%;background:var(--sky);margin:0 auto 14px}
  .brand-name{font:700 27px "Montserrat",sans-serif;color:#2a6fb6;letter-spacing:.5px}
  .brand-sub{font:700 14px "Montserrat",sans-serif;color:#2a6fb6;letter-spacing:2px;margin-top:2px}
  .title-band{left:0;top:330px;width:1000px;height:95px;background:var(--band);text-align:center;font:400 76px/95px "Open Sans",sans-serif;letter-spacing:1px}
  .rule-green{left:0;top:425px;width:1000px;height:15px;background:var(--green)}
  .tagline{left:0;top:440px;width:1000px;height:36px;background:var(--sky);text-align:center;font:700 23px/36px "Montserrat",sans-serif;letter-spacing:.5px}
  .headline{left:0;top:480px;width:1000px;text-align:center;font:800 62px/80px "Montserrat",sans-serif;letter-spacing:1px}
  .walker{left:45px;top:555px;width:230px;height:570px;border-radius:110px 110px 30px 30px;background:linear-gradient(180deg,#2eaee4,#27a4dc)}
  .symptom{background:var(--sky);font:700 25px/30px "Montserrat",sans-serif;padding:0 6px;letter-spacing:.5px;box-shadow:4px 4px 6px rgba(0,0,0,.25)}
  .chart{left:660px;top:550px;width:300px;height:280px}
  .usage{left:495px;top:838px;width:480px;height:110px}
  .usage-copy{left:625px;top:848px;font:400 19px/30px "Open Sans",sans-serif;letter-spacing:.8px}
  .usage-copy strong{display:block;font:700 28px/32px "Montserrat",sans-serif;letter-spacing:.5px}
  .benefit{left:0;top:965px;width:1000px;height:75px;background:var(--teal)}
  .benefit p{position:absolute;right:20px;font:600 18.5px/20px "Montserrat",sans-serif;letter-spacing:.7px}
  .benefit strong{font-weight:800}
  .doctor{left:0;top:1040px;width:1000px;height:165px;background:var(--green);text-align:center}
  .doctor-name{padding-top:32px;font:700 31px/36px "Montserrat",sans-serif;letter-spacing:1px}
  .doctor-role{font:700 23px/32px "Montserrat",sans-serif;letter-spacing:1px}
  .doctor-place{margin-top:18px;font:700 21px/26px "Montserrat",sans-serif;letter-spacing:.8px}
  .offer{left:0;top:1205px;width:1000px;height:75px;background:var(--teal);text-align:center;font:800 21px/32px "Montserrat",sans-serif;letter-spacing:.8px;padding-top:6px}
  .offer span{font:400 19px "Open Sans",sans-serif}
  .offer .url{font-size:24px}
  .footer-strip{left:0;top:1280px;width:1000px;height:14px;background:var(--blue)}
</style>
</head>
<body>
<main class="flyer">
  <div class="abs hero-photo" role="img" aria-label="Photo of a woman at a desk with a laptop, stretching her aching back"></div>

  <div class="abs brand">
    <div class="brand-mark"></div>
    <div class="brand-name">SPINE EASE CLINIC</div>
    <div class="brand-sub">DR SAM WHITFORD - CHIROPRACTOR</div>
  </div>

  <h1 class="abs title-band">SPINE EASE CLINIC</h1>
  <div class="abs rule-green"></div>
  <p class="abs tagline">AS THE HEAD TILTS FORWARD, MORE FORCE IS PLACED ON THE SPINE</p>
  <h2 class="abs headline">TECH NECK</h2>

  <div class="abs walker" role="img" aria-label="Silhouette of a person walking while looking down at a phone"></div>

  <span class="abs symptom" style="left:203px;top:575px">HEADACHES</span>
  <span class="abs symptom" style="left:188px;top:625px">NECK PAIN</span>
  <span class="abs symptom" style="left:183px;top:675px">SHOULDER PAIN</span>
  <span class="abs symptom" style="left:228px;top:727px">BACK PAIN</span>
  <span class="abs symptom" style="left:183px;top:779px">ARM &amp; HAND PAIN</span>
  <span class="abs symptom" style="left:178px;top:829px">SCIATICA</span>

  <svg class="abs chart" viewBox="660 550 300 280" aria-label="Pressure on spine by degrees of forward head tilt">
    <g fill="var(--sky)">
      <rect x="675" y="720" width="34" height="56"/>
      <rect x="725" y="672" width="34" height="104"/>
      <rect x="777" y="630" width="34" height="146"/>
      <rect x="828" y="594" width="33" height="182"/>
      <rect x="878" y="558" width="33" height="218"/>
    </g>
    <g fill="#fff" font-family="Montserrat, sans-serif" font-weight="700" font-size="20" text-anchor="middle">
      <text x="692" y="752">12</text>
      <text x="742" y="723">27</text>
      <text x="794" y="696">40</text>
      <text x="844" y="667">49</text>
      <text x="894" y="639">60</text>
      <text x="692" y="797">0º</text>
      <text x="744" y="797">15º</text>
      <text x="796" y="797">30º</text>
      <text x="847" y="797">45º</text>
      <text x="898" y="797">60º</text>
      <text x="800" y="820" font-size="14.5" letter-spacing=".6">DEGREES OF FORWARD HEAD TILT</text>
      <text transform="translate(942 668) rotate(-90)" font-size="13.5" letter-spacing=".6">PRESSURE ON SPINE (LBS)</text>
    </g>
  </svg>

  <svg class="abs usage" viewBox="495 838 480 110" aria-label="Pie chart of daily device use">
    <circle cx="550" cy="893" r="52" fill="var(--sky)"/>
    <path d="M550 893 L550 841 A52 52 0 0 1 586 931 Z" fill="var(--teal)"/>
  </svg>
  <p class="abs usage-copy">THE AVERAGE PERSON SPENDS<strong>8-10 HOURS PER DAY</strong>USING ELECTRONIC DEVICES</p>

  <section class="abs benefit">
    <p style="top:10px"><strong>CHIROPRACTIC</strong> CAN HELP <strong>CORRECT</strong> AND <strong>PREVENT</strong> THESE PROBLEMS BY</p>
    <p style="top:49px"><strong>RESTORING</strong> AND <strong>MAINTAINING</strong> PROPER ALIGNMENT OF THE NECK</p>
  </section>

  <section class="abs doctor">
    <p class="doctor-name">DR SAM WHITFORD</p>
    <p class="doctor-role">CHIROPRACTOR</p>
    <p class="doctor-place">NOW IN SOUTHPORT AT 42 HARBOUR RD - ATRIUM SUITES</p>
  </section>

  <section class="abs offer">
    <p>50% OFF INITIAL CONSULTATION IF YOU BOOK ONLINE AT</p>
    <p><span class="url" style="font:800 24px Montserrat,sans-serif">WWW.SPINEEASECLINIC.COM.AU</span> <span>(CHOOSE TECH NECK OPTION)</span></p>
  </section>
  <div class="abs footer-strip"></div>
</main>
</body>
</html>
```